Kelvanta (www.kelvanta.net) needs exciting professional PowerPoint pitch template

Kelvanta is an exciting new start-up targeting innovative ways to engage with retail customers at the point of sale.

Our customers are looking for us to help them increase the "wallet share" of their retail customers. The retail customer has their wallet open at the Point of Sale and are paying money to our customer. At Kelvanta we are all about attracting the attention of the retail customer AT THAT POINT IN TIME and engaging the retail customer in spending a little more in that store or another store that has a relationship to the retail customer's purchase.

Our customers are the owners of very large supermarkets, chain stores, and financial institutions, and therefore when we pitch a proposal to these buyers it needs to be slick, professional, and very memorable.

The PowerPoint sales presentation template is a key part of striking that impression.

Here is some background...

Our Vision
Through applying new thinking to a mature industry we are reinventing selected segments of the Australian retail messaging business, generating significant value for our customers, our suppliers, and our owners.
We operate with integrity, agility, and intelligence to doing things smarter, faster and more efficiently.
We bring deep industry expertise, deep relationships with customers and suppliers, and a will to see the old ways give way to smarter ways – this is why we win.
From this economically sustainable platform, we will examine the disruption of other market segments by further leveraging the elements that make us successful.

Our Values
With our clients, with our suppliers, with our staff, and with our owners:
# We Partner – We align the interest of all stakeholders by striving to ensure everything we do is mutually beneficial and commercially sustainable in the long term. We are clear with all our stakeholders about what our expectations are of them, and we seek clarity from them in their expectations of us.
# We Innovate – In the segments we choose to compete in, we bring fresh ideas, new business processes, the right relationships, and the right technology to ensure the supply chain is nimble, competitive, and reliable.
# We are Accountable – We say what we will do, and then do what we say.
# We Perform – We use our skills, relationships, and reputation to deliver value to our customers, suppliers, and owners.

Initially we are building our business from low-tech through printing promotional offers and retailer messages on ATM and EFTPOS receipts, but as soon as cash flow supports it we will be engaging in high-tech real-time targeted offers to the specific consumer through video wall offers as people are at the checkout or walking through the shopping centre.

I'd like the PowerPoint template to reflect our vision and values.

The PowerPoint template will be used in communicating our proposals to our clients, and needs to catch and hold our audiences attention.

Please check out the web site we have just launched - it is pretty basic but it has only been up a week. We intend to sharpen it over the coming weeks, but you'll get the idea of what our core messages are.

I have recently sourced a logo from ArtHarbor, plus business cards, and have attached the source files for your reference.
Updates

Hi everybody.  Thanks for the designs submitted so far.  Your submissions have helped me understand what I do and don't prefer, and I have updated the "Must Have/Nice to Have/Shouldn't Have" criteria accordingly.  I have also uploaded a powerpoint template that I had at a company I udsed to run that has the sort of visual theme I find appealing. I have more time to provide feedback now that the week is over, so I will comment on individual designs shortly, and I will respond to queries directed to me.

Kind Regards - Grant

Target Market(s)

Our customers are large corporations that have professional Point Of Sale marketing experts looking for a supplier with an edge over others in a crowded market. The buyer of our product and services is ultimately a communications expert. They want to see distinctive competence, and an agility of thinking that will make them money through driving more consumer spending.

Industry/Entity Type

Financial

Font styles to use
Sans Serif

Colors
34a7d7
0892cd
3276b5

Requirements
Must have
• The following Slides: Title Slide, Agenda, About Kelvanta, Thank you
The pages must be easy on the eye.
The final product must be a PowerPoint template file with the usual "Title", "Title and Content", "Title & Table", and "Blank" page types.
Widescreen format please.
Nice to have
• The pages should have an eye-catching visual element running through all the pages. I have attached a template from a company i used to be involved with that has a visual theme running through it that I like.
Plenty of whitespace - have a look at www.kelvanta.net.
Bonus points for pulling the text from the brief into the template.
Use "Innovation - Integrity - Service" as the tag line.
Should not have
• Pages should not be busy.
Stay away from too much black. I know the cards have black, but the presentation shouldn't.
I dont like serifed fonts. Use Dravelle's Modern UI style for insporation.
The "Bringing Lumora" tag line was an invention of the logo designer that we do not want to cary forward. Please do not use it.

```html
<!DOCTYPE html>
<html lang="en">
<head>
<meta charset="utf-8">
<title>Sample Design V1 – Kelvanta Presentation Template</title>
<link rel="stylesheet" href="https://fonts.googleapis.com/css2?family=Arimo:wght@400;700&family=Carlito&display=swap">
<style>
  :root {
    --board-bg: #a6a6a6;
    --slide-bg: #ffffff;
    --ink: #1a1a1a;
    --muted: #7a7a7a;
    --brand: #0892cd;
    --brand-sky: #34a7d7;
    --brand-deep: #3276b5;
    --navy: #0b3a6e;
    --mid: #0a7cc4;
    --soft: #6a9bd1;
    --pale: #a9d3f3;
    --grid: #c8c8c8;
  }
  * { margin: 0; padding: 0; box-sizing: border-box; }
  html, body { width: 1200px; height: 900px; overflow: hidden; }
  body { background: var(--board-bg); font-family: "Arimo", Arial, sans-serif; }
  .board { position: relative; width: 1200px; height: 900px; }
  .board-title {
    position: absolute; top: 80px; left: 0; width: 1200px; text-align: center;
    font-family: "Carlito", "Calibri", sans-serif; font-size: 27px; font-weight: 400; color: #000;
  }
  .slide { position: absolute; width: 346px; height: 259px; background: var(--slide-bg); display: block; }
  .slide text { font-family: "Arimo", Arial, sans-serif; }
  .s-title { left: 35px; top: 192px; }
  .s-bullets { left: 425px; top: 192px; }
  .s-pie { left: 814px; top: 192px; }
  .s-line { left: 35px; top: 502px; }
  .s-bar { left: 425px; top: 498px; }
  .s-thanks { left: 814px; top: 502px; }
  .heading { font-size: 13px; fill: var(--ink); }
  .label { font-size: 5px; fill: #333; }
  .axis { stroke: var(--grid); stroke-width: 0.6; }
  .brand-word { font-weight: 700; fill: var(--brand); }
</style>
</head>
<body>
<main class="board">
  <h1 class="board-title">Sample Design V1</h1>

  <svg class="slide s-title" viewBox="0 0 346 259" aria-label="Title slide">
    <defs>
      <linearGradient id="bubbleWash" x1="0" y1="0" x2="0" y2="1">
        <stop offset="0" stop-color="#6fb4e0"/>
        <stop offset="0.7" stop-color="#b4daf2"/>
        <stop offset="1" stop-color="#ffffff"/>
      </linearGradient>
      <linearGradient id="cornerWash" x1="0" y1="0" x2="1" y2="1">
        <stop offset="0" stop-color="#7dbbe4"/>
        <stop offset="1" stop-color="#ffffff"/>
      </linearGradient>
    </defs>
    <rect x="0" y="0" width="346" height="150" fill="url(#bubbleWash)" role="img" aria-label="Decorative cluster of overlapping blue bubbles"/>
    <text class="brand-word" x="56" y="131" font-size="18">Kelvanta</text>
    <text x="173" y="192" text-anchor="middle" font-size="11.5" fill="var(--brand-deep)">Presentation Template</text>
    <text x="173" y="206" text-anchor="middle" font-size="6" fill="var(--muted)">November 15, 2013</text>
  </svg>

  <svg class="slide s-bullets" viewBox="0 0 346 259" aria-label="Title and content slide">
    <rect x="0" y="0" width="30" height="24" fill="url(#cornerWash)" role="img" aria-label="Small bubble accent"/>
    <text class="heading" x="20" y="48">Title and Bulleted Content</text>
    <g font-size="8.5" fill="var(--ink)">
      <text x="20" y="71">•  Click to edit Master text styles</text>
      <text x="36" y="83">–  Second level</text>
      <text x="54" y="96" font-size="8">•  Third level</text>
      <text x="72" y="108" font-size="8">–  Fourth level</text>
      <text x="88" y="120" font-size="8">»  Fifth level</text>
    </g>
    <text class="brand-word" x="336" y="255" font-size="8" text-anchor="end">Kelvanta</text>
  </svg>

  <svg class="slide s-pie" viewBox="0 0 346 259" aria-label="Pie chart slide">
    <rect x="0" y="0" width="30" height="24" fill="url(#cornerWash)" role="img" aria-label="Small bubble accent"/>
    <text class="heading" x="20" y="47">Pie Chart</text>
    <text x="174" y="77" text-anchor="middle" font-size="10" fill="var(--ink)">Chart Title</text>
    <path d="M174 153 L174 101 A52 52 0 1 1 148.95 198.57 Z" fill="var(--navy)" stroke="#fff" stroke-width="0.6"/>
    <path d="M174 153 L148.95 198.57 A52 52 0 0 1 125.65 133.86 Z" fill="var(--soft)" stroke="#fff" stroke-width="0.6"/>
    <path d="M174 153 L125.65 133.86 A52 52 0 0 1 146.14 109.1 Z" fill="var(--pale)" stroke="#fff" stroke-width="0.6"/>
    <path d="M174 153 L146.14 109.1 A52 52 0 0 1 174 101 Z" fill="var(--mid)" stroke="#fff" stroke-width="0.6"/>
    <g font-size="6.5" fill="#333" text-anchor="middle">
      <text x="241" y="169">1st Qtr</text><text x="241" y="177">58%</text>
      <text x="106" y="172">2nd Qtr</text><text x="106" y="180">23%</text>
      <text x="119" y="110">3rd Qtr</text><text x="119" y="118">10%</text>
      <text x="158" y="92">4th Qtr</text><text x="158" y="100">9%</text>
    </g>
    <text class="brand-word" x="336" y="255" font-size="8" text-anchor="end">Kelvanta</text>
  </svg>

  <svg class="slide s-line" viewBox="0 0 346 259" aria-label="Line chart slide">
    <rect x="0" y="0" width="30" height="24" fill="url(#cornerWash)" role="img" aria-label="Small bubble accent"/>
    <text class="heading" x="20" y="47">Line Chart</text>
    <g class="label" text-anchor="end">
      <text x="44" y="197">0</text><text x="44" y="184">0.5</text><text x="44" y="170">1</text>
      <text x="44" y="157">1.5</text><text x="44" y="144">2</text><text x="44" y="130">2.5</text>
      <text x="44" y="117">3</text><text x="44" y="104">3.5</text><text x="44" y="90">4</text>
      <text x="44" y="77">4.5</text><text x="44" y="64">5</text>
    </g>
    <line class="axis" x1="48" y1="62" x2="48" y2="195"/>
    <line class="axis" x1="48" y1="195" x2="250" y2="195"/>
    <g class="label" text-anchor="middle">
      <text x="73" y="204">Category 1</text><text x="124" y="204">Category 2</text>
      <text x="175" y="204">Category 3</text><text x="226" y="204">Category 4</text>
    </g>
    <g fill="none" stroke-width="1">
      <polyline points="73,80.6 124,128.5 175,101.9 226,75.3" stroke="var(--pale)"/>
      <polyline points="73,131.2 124,78 175,147.1 226,120.5" stroke="var(--navy)"/>
      <polyline points="73,168.4 124,163.1 175,125.8 226,155.1" stroke="var(--mid)"/>
      <polyline points="73,184.4 124,104.6 175,75.3 226,96.6" stroke="var(--soft)"/>
    </g>
    <g>
      <g fill="var(--pale)"><circle cx="73" cy="80.6" r="1.6"/><circle cx="124" cy="128.5" r="1.6"/><circle cx="175" cy="101.9" r="1.6"/><circle cx="226" cy="75.3" r="1.6"/></g>
      <g fill="var(--navy)"><circle cx="73" cy="131.2" r="1.6"/><circle cx="124" cy="78" r="1.6"/><circle cx="175" cy="147.1" r="1.6"/><circle cx="226" cy="120.5" r="1.6"/></g>
      <g fill="var(--mid)"><circle cx="73" cy="168.4" r="1.6"/><circle cx="124" cy="163.1" r="1.6"/><circle cx="175" cy="125.8" r="1.6"/><circle cx="226" cy="155.1" r="1.6"/></g>
      <g fill="var(--soft)"><circle cx="73" cy="184.4" r="1.6"/><circle cx="124" cy="104.6" r="1.6"/><circle cx="175" cy="75.3" r="1.6"/><circle cx="226" cy="96.6" r="1.6"/></g>
    </g>
    <g class="label" text-anchor="middle">
      <text x="73" y="73">4.3</text><text x="124" y="122">2.5</text><text x="175" y="95">3.5</text><text x="226" y="68">4.5</text>
      <text x="73" y="125">2.4</text><text x="124" y="71">4.4</text><text x="175" y="141">1.8</text><text x="226" y="114">2.8</text>
      <text x="73" y="162">1</text><text x="124" y="157">1.2</text><text x="175" y="119">2.6</text><text x="226" y="149">1.5</text>
    </g>
    <g font-size="7" fill="#222" text-anchor="middle">
      <text x="73" y="178">0.4</text><text x="124" y="98">3.4</text><text x="175" y="68">4.5</text><text x="226" y="90">3.7</text>
    </g>
    <g class="label">
      <line x1="262" y1="152" x2="270" y2="152" stroke="var(--pale)" stroke-width="0.8"/><circle cx="266" cy="152" r="1.6" fill="var(--pale)"/><text x="273" y="154">Series 1</text>
      <line x1="262" y1="161" x2="270" y2="161" stroke="var(--navy)" stroke-width="0.8"/><circle cx="266" cy="161" r="1.6" fill="var(--navy)"/><text x="273" y="163">Series 2</text>
      <line x1="262" y1="170" x2="270" y2="170" stroke="var(--mid)" stroke-width="0.8"/><circle cx="266" cy="170" r="1.6" fill="var(--mid)"/><text x="273" y="172">Series 3</text>
      <line x1="262" y1="179" x2="270" y2="179" stroke="var(--soft)" stroke-width="0.8"/><circle cx="266" cy="179" r="1.6" fill="var(--soft)"/><text x="273" y="181">Series 4</text>
    </g>
    <text class="brand-word" x="336" y="255" font-size="8" text-anchor="end">Kelvanta</text>
  </svg>

  <svg class="slide s-bar" viewBox="0 0 346 259" aria-label="Bar chart slide">
    <rect x="0" y="0" width="30" height="24" fill="url(#cornerWash)" role="img" aria-label="Small bubble accent"/>
    <text class="heading" x="20" y="46">Bar Chart</text>
    <g class="label" text-anchor="end">
      <text x="64" y="194">0</text><text x="64" y="178">1</text><text x="64" y="161">2</text>
      <text x="64" y="145">3</text><text x="64" y="129">4</text><text x="64" y="113">5</text>
      <text x="64" y="96">6</text><text x="64" y="80">7</text>
    </g>
    <line class="axis" x1="68" y1="78" x2="68" y2="192"/>
    <line class="axis" x1="68" y1="192" x2="262" y2="192"/>
    <g>
      <rect x="79" y="121.9" width="7" height="70.1" fill="var(--mid)"/>
      <rect x="86" y="152.9" width="7" height="39.1" fill="var(--pale)"/>
      <rect x="93" y="159.4" width="7" height="32.6" fill="var(--navy)"/>
      <rect x="100" y="110.5" width="7" height="81.5" fill="var(--soft)"/>
      <rect x="127" y="151.25" width="7" height="40.75" fill="var(--mid)"/>
      <rect x="134" y="120.3" width="7" height="71.7" fill="var(--pale)"/>
      <rect x="141" y="143.1" width="7" height="48.9" fill="var(--navy)"/>
      <rect x="148" y="130.1" width="7" height="61.9" fill="var(--soft)"/>
      <rect x="175" y="134.95" width="7" height="57.05" fill="var(--mid)"/>
      <rect x="182" y="162.7" width="7" height="29.3" fill="var(--pale)"/>
      <rect x="189" y="94.2" width="7" height="97.8" fill="var(--navy)"/>
      <rect x="196" y="146.4" width="7" height="45.6" fill="var(--soft)"/>
      <rect x="223" y="118.65" width="7" height="73.35" fill="var(--mid)"/>
      <rect x="230" y="146.4" width="7" height="45.6" fill="var(--pale)"/>
      <rect x="237" y="110.5" width="7" height="81.5" fill="var(--navy)"/>
      <rect x="244" y="139.8" width="7" height="52.2" fill="var(--soft)"/>
    </g>
    <g class="label" text-anchor="middle">
      <text x="82.5" y="119">4.3</text><text x="89.5" y="150">2.4</text><text x="96.5" y="157">2</text><text x="103.5" y="108">5</text>
      <text x="130.5" y="148">2.5</text><text x="137.5" y="117">4.4</text><text x="144.5" y="140">3</text><text x="151.5" y="127">3.8</text>
      <text x="178.5" y="132">3.5</text><text x="185.5" y="160">1.8</text><text x="192.5" y="91">6</text><text x="199.5" y="143">2.8</text>
      <text x="226.5" y="116">4.5</text><text x="233.5" y="143">2.8</text><text x="240.5" y="108">5</text><text x="247.5" y="137">3.2</text>
      <text x="93" y="202">A</text><text x="141" y="202">B</text><text x="189" y="202">C</text><text x="237" y="202">D</text>
    </g>
    <g class="label">
      <rect x="271" y="122" width="2.5" height="2.5" fill="var(--mid)"/><text x="276" y="125">S1</text>
      <rect x="271" y="132" width="2.5" height="2.5" fill="var(--pale)"/><text x="276" y="135">S2</text>
      <rect x="271" y="142" width="2.5" height="2.5" fill="var(--navy)"/><text x="276" y="145">S3</text>
      <rect x="271" y="152" width="2.5" height="2.5" fill="var(--soft)"/><text x="276" y="155">S4</text>
    </g>
    <text class="brand-word" x="336" y="255" font-size="8" text-anchor="end">Kelvanta</text>
  </svg>

  <svg class="slide s-thanks" viewBox="0 0 346 259" aria-label="Thank you slide">
    <rect x="0" y="0" width="346" height="150" fill="url(#bubbleWash)" role="img" aria-label="Decorative cluster of overlapping blue bubbles"/>
    <text class="brand-word" x="56" y="129" font-size="18">Kelvanta</text>
    <text x="173" y="192" text-anchor="middle" font-size="11.5" fill="var(--brand-deep)">Thank You</text>
    <text x="173" y="206" text-anchor="middle" font-size="6" fill="var(--muted)">November 15, 2013</text>
  </svg>
</main>
</body>
</html>
```